Give us a remarkable appearance

We need a unique, remarkable stationery design (Business Cards, Business Letters, Email Signature etc.). The design should use our logo.

Verlan-Consulting is a startup in consulting, management and IT services and individual software development for the financial industry.

Verlan in english is agate stone. We would like to see designs that use colors out of the agate stone color range.

Preferred COLORS: gold, dark red (burgundy), white, dark grey, black ** see attached Logos **

The used font should be available for further usage with texts etc.

The design should express: modernity, precious, high quality, lightness, stability, ecological awareness, speedy, reliability, simplicity, sustainability.

Target Market(s)

C-Level and Business Clients, Professionals

Industry/Entity Type

Business

Logo Text

Logo styles of interest
Pictorial/Combination Logo
Abstract Logo
Wordmark Logo
Requirements
Must have
• Business Cards, Business Papers, Email Signature
Nice to have
• Door plate, Flyersheet (basic structure), Envelop...

```html
<!DOCTYPE html>
<html lang="en">
<head>
<meta charset="utf-8">
<title>Verlan Consulting – Stationery Set</title>
<link rel="stylesheet" href="https://fonts.googleapis.com/css2?family=Questrial&family=Saira:wght@400;600&display=swap">
<style>
  :root{
    --bg:#3b3b3d;
    --paper:#ffffff;
    --gold:#f2c811;
    --gold-deep:#e2b408;
    --gold-pale:#f8e27a;
    --ink:#1a1a1a;
    --rule:#c9c9c9;
    --cell:#e6e6e6;
    --label:#8a8a8a;
  }
  *{box-sizing:border-box;margin:0;padding:0}
  html,body{width:1200px;height:1000px;overflow:hidden}
  body{background:var(--bg);position:relative;font-family:"Questrial",sans-serif;color:var(--ink)}
  .piece{position:absolute;background:var(--paper);overflow:hidden}

  .brand{position:absolute;display:flex;align-items:center;gap:10px;color:var(--gold-deep);font-family:"Questrial",sans-serif}
  .brand-dot{border-radius:50%;background:var(--gold-deep);flex:none}
  .brand-name{display:flex;flex-direction:column;line-height:1}
  .brand-name .word{letter-spacing:.32em}
  .brand-name .sub{letter-spacing:.28em;text-transform:lowercase}
  .brand.on-gold{color:#fff}
  .brand.on-gold .brand-dot{background:#fff}

  .band{position:absolute;left:0;right:0;bottom:0;
    background:linear-gradient(180deg,var(--gold-pale) 0,var(--gold-pale) 18%,#f5d640 18%,#f5d640 36%,var(--gold) 36%)}

  .letterhead{left:35px;top:62px;width:350px;height:493px}
  .letterhead .band{height:35px}
  .letterhead .url{position:absolute;left:0;right:0;bottom:11px;text-align:center;font-family:"Saira",sans-serif;font-size:11px;letter-spacing:.04em}

  .invoice{left:401px;top:62px;width:351px;height:493px}
  .field{position:absolute;font-size:5px;color:var(--label)}
  .line{position:absolute;height:1px;background:var(--rule)}
  .table{position:absolute;left:21px;top:162px;width:309px;height:194px;border:1px solid var(--rule);
    background:repeating-linear-gradient(180deg,transparent 0,transparent 10px,var(--rule) 10px,var(--rule) 11px)}
  .table-head{height:14px;background:#222;color:#bbb;font-size:5px;display:flex;align-items:center;padding:0 8px;justify-content:space-between}
  .table-head span:last-child{width:72px}
  .table .col{position:absolute;top:0;bottom:0;left:227px;width:1px;background:var(--rule)}
  .totals{position:absolute;left:249px;top:357px;width:81px}
  .totals div{position:relative;height:10px;margin-bottom:1px;background:var(--cell)}
  .totals span{position:absolute;right:86px;top:2px;font-size:5px;color:var(--label);white-space:nowrap}
  .invoice .band{height:35px}
  .foot{position:absolute;bottom:9px;display:flex;gap:8px;font-family:"Saira",sans-serif;font-size:5px;line-height:1.5;white-space:nowrap}
  .foot .sep{width:1px;background:#444;align-self:stretch}
  .foot .right{text-align:right}

  .card-back{left:767px;top:71px;width:400px;height:229px;background:linear-gradient(180deg,var(--gold) 0,var(--gold) 70%,var(--gold-deep) 100%)}

  .card-front{left:767px;top:315px;width:400px;height:229px}
  .card-front .panel{position:absolute;left:0;right:0;top:95px;bottom:0;background:linear-gradient(180deg,var(--gold) 0,#f3cf2a 45%,var(--gold-deep) 100%)}
  .contact{position:absolute;color:#fff;font-family:"Saira",sans-serif;font-weight:600;font-size:9.5px;line-height:1.25;white-space:nowrap}
  .contact .role{font-weight:400;font-size:8px}
  .divider{position:absolute;width:1px;background:rgba(255,255,255,.7)}

  .slip{left:35px;top:599px;width:500px;height:149px}
  .slip .band{height:68px}
  .slip .foot{font-size:10px;bottom:18px;left:26px;gap:14px}

  .env-back{left:451px;top:788px;width:350px;height:152px}
  .env-front{left:817px;top:790px;width:350px;height:150px}
  .env-front .band{height:25px}
  .flap{position:absolute}
</style>
</head>
<body>

<section class="piece letterhead">
  <div class="brand" style="left:40px;top:200px">
    <span class="brand-dot" style="width:28px;height:28px"></span>
    <span class="brand-name"><span class="word" style="font-size:34px">VERLAN</span><span class="sub" style="font-size:19px;margin-top:4px">consulting</span></span>
  </div>
  <div class="band"></div>
  <div class="url">WWW.VERLANCONSULTING.COM</div>
</section>

<section class="piece invoice">
  <div class="brand" style="left:21px;top:16px;gap:6px">
    <span class="brand-dot" style="width:12px;height:12px"></span>
    <span class="brand-name"><span class="word" style="font-size:14px">VERLAN</span><span class="sub" style="font-size:8px;margin-top:2px">consulting</span></span>
  </div>
  <span class="field" style="left:21px;top:95px">sold to</span>
  <span class="field" style="left:197px;top:95px">Ship to</span>
  <div class="line" style="left:38px;top:98px;width:113px"></div>
  <div class="line" style="left:21px;top:110px;width:130px"></div>
  <div class="line" style="left:21px;top:121px;width:130px"></div>
  <div class="line" style="left:21px;top:132px;width:130px"></div>
  <div class="line" style="left:21px;top:142px;width:130px"></div>
  <div class="line" style="left:216px;top:98px;width:114px"></div>
  <div class="line" style="left:197px;top:110px;width:133px"></div>
  <div class="line" style="left:197px;top:121px;width:133px"></div>
  <div class="line" style="left:197px;top:132px;width:133px"></div>
  <div class="line" style="left:197px;top:142px;width:133px"></div>

  <div class="table">
    <div class="table-head"><span>Quantity</span><span>Amount</span></div>
    <div class="col"></div>
  </div>
  <div class="totals">
    <div><span>Shipping</span></div>
    <div><span>Sub Total</span></div>
    <div><span>Deposit</span></div>
    <div><span>Balance Due</span></div>
    <div><span>Total</span></div>
  </div>
  <span class="field" style="left:26px;top:378px">Signature:</span>
  <div class="line" style="left:56px;top:381px;width:104px"></div>
  <span class="field" style="left:26px;top:405px">Date:</span>
  <div class="line" style="left:42px;top:408px;width:118px"></div>

  <div class="band"></div>
  <div class="foot" style="left:52px">
    <div class="right">18 ELM ROW, THIRD FLOOR<br>RIVERTON, 48210</div><span class="sep"></span>
    <div>T : 0555 8102934<br>F : 0555 8102935</div><span class="sep"></span>
    <div>E : INFO@VERLANCONSULTING.COM<br>W: WWW.VERLANCONSULTING.COM</div>
  </div>
</section>

<section class="piece card-back">
  <div class="brand on-gold" style="left:28px;top:80px;gap:14px">
    <span class="brand-dot" style="width:36px;height:36px"></span>
    <span class="brand-name"><span class="word" style="font-size:38px">VERLAN</span><span class="sub" style="font-size:19px;margin-top:6px">consulting</span></span>
  </div>
</section>

<section class="piece card-front">
  <div class="brand" style="left:20px;top:24px">
    <span class="brand-dot" style="width:22px;height:22px"></span>
    <span class="brand-name"><span class="word" style="font-size:25px">VERLAN</span><span class="sub" style="font-size:14px;margin-top:3px">consulting</span></span>
  </div>
  <div class="panel"></div>
  <div class="contact" style="left:80px;top:126px">ALEX MARLOW<br><span class="role">Owner</span></div>
  <div class="contact" style="left:80px;top:170px;font-size:9px;line-height:1.7">18 Elm Row, Third Floor<br>Riverton, 48210</div>
  <div class="divider" style="left:227px;top:124px;height:80px"></div>
  <div class="contact" style="left:233px;top:126px;font-size:9px;line-height:2.3">T : 0555 8102934<br>F : 0555 8102935<br>E : info@verlanconsulting.com<br>WWW.VERLANCONSULTING.COM</div>
</section>

<section class="piece slip">
  <div class="brand" style="left:30px;top:12px;gap:12px">
    <span class="brand-dot" style="width:28px;height:28px"></span>
    <span class="brand-name"><span class="word" style="font-size:34px">VERLAN</span><span class="sub" style="font-size:20px;margin-top:4px">consulting</span></span>
  </div>
  <div class="band"></div>
  <div class="foot">
    <div class="right">18 ELM ROW, THIRD FLOOR<br>RIVERTON, 48210</div><span class="sep"></span>
    <div>T : 0555 8102934<br>F : 0555 8102935</div><span class="sep"></span>
    <div>E : INFO@VERLANCONSULTING.COM<br>W: WWW.VERLANCONSULTING.COM</div>
  </div>
</section>

<section class="piece env-back">
  <svg class="flap" width="350" height="60" viewBox="0 0 350 60" aria-hidden="true">
    <path d="M0 0 H350 L342 26 Q338 32 330 33 L175 57 L20 33 Q12 32 8 26 Z" fill="var(--gold)"/>
    <circle cx="175" cy="38" r="7" fill="#fff"/>
  </svg>
</section>

<svg class="flap" style="left:817px;top:730px" width="350" height="61" viewBox="0 0 350 61" aria-hidden="true">
  <path d="M0 61 L8 34 Q12 28 22 26 L175 0 L328 26 Q338 28 342 34 L350 61 Z" fill="var(--gold)"/>
  <circle cx="175" cy="18" r="7" fill="#fff"/>
</svg>
<section class="piece env-front">
  <div class="brand" style="left:14px;top:10px;gap:6px">
    <span class="brand-dot" style="width:12px;height:12px"></span>
    <span class="brand-name"><span class="word" style="font-size:15px">VERLAN</span><span class="sub" style="font-size:8px;margin-top:2px">consulting</span></span>
  </div>
  <div class="band"></div>
</section>

</body>
</html>
```